Finbrawl 2014 Carp Fishing Tournament Presented by Bramblewick Fly Fishing

I need a promotional poster for a Carp fishing tournament that will take place in the Minneapolis/St.Paul area on June 21st 2014.
The tournament is open to anyone but it is fly fishing only. The cost to compete is $25 and proceeds will benefit Riverbed Keepers. It is a fun tournament with no cash prizes but there will be a raffle and prizes for biggest fish caught, ugliest fish caught, and most fish caught.
Bramblewick Fly Fishing Co. is my company and the poster should be branded with my logo and take inspiration from the overall feel of the brand but it doesn't have to be too similar. I'm definitely open to new designs and ideas. Here is a link to my website for review - www.bramblewickflyfishing.example.
I'm not sure about the meeting place for the kickoff and award presentation but will have that nailed down very soon.

We will be adding sponsor logos to the bottom of the poster as we get them so there should be space for that somewhere if possible.
Our biggest supporter is Scalewise Magazine (logo attached) Their logo should be placed prominently on the poster but smaller than Bramblewick Fly Fishing.

I have now guaranteed payment for this project. 

Please read my brief more carefully and look at the example of the concert poster link i added to the brief.

For some reason my brief is not updating when I save and update so I'm going to write an update here and hopefully this will be seen by all designers.

I no longer want a homicide or need guns in the poster as stated previously in my " Nice to Have" section

- It would be great if we could have a carp actually committing a homicide on the poster. Possibly a carp with a gun shooting at another carp? or a fisherman getting shot by a carp?

we have desided that this is just to gnarly for the general public. Please let me know if you have any questions.

Target Market(s)

Think Skateboarding or old punk rock album covers like the Dreggs, Rust Lantern, or the Gobbets, old concert posters are also something I like and can be used for inspiration
http://img-store-qx4.pictoboard.example/236x/c2/17/9a/c2179a61f03d7e4b8a2c55d0e91bd406.jpg

Industry/Entity Type

It Company

Requirements
Must have
• Must clearly show cost, and have Bramblewick Fly Fishing logo and Scalewise logos showing.
Nice to have
• It would be great if we could have a carp actually committing a homicide on the poster. Possibly a carp with a gun shooting at another carp? or a fisherman getting shot by a carp?
Should not have
• Should not have any pictures of someone fishing with a SPINNING ROD.

```html
<!DOCTYPE html>
<html lang="en">
<head>
<meta charset="utf-8">
<title>Finbrawl 2014 Carp Fishing Tournament</title>
<link href="https://fonts.googleapis.com/css2?family=Delius&display=swap" rel="stylesheet">
<style>
  :root {
    --page-bg: #e4e4e4;
    --paper: #eef3f6;
    --paper-edge: #ffffff;
    --navy: #27356a;
    --sage: #8c9888;
    --badge-brown: #4a3530;
    --badge-shadow: #8e9a8c;
    --ribbon-tan: #d9b88a;
    --cream: #f3e7cf;
    --brand-dark: #2a2321;
    --sponsor-orange: #d9731f;
  }
  * { margin: 0; padding: 0; box-sizing: border-box; }
  html, body { width: 1200px; height: 900px; overflow: hidden; }
  body {
    background: var(--page-bg);
    font-family: "Delius", "Comic Neue", cursive;
    position: relative;
  }
  .poster {
    position: absolute;
    left: 337px; top: 47px;
    width: 524px; height: 806px;
    background: linear-gradient(180deg, #d9e6ee 0%, #e6eef3 55%, var(--paper) 90%);
    overflow: hidden;
    box-shadow: 0 2px 6px rgba(0,0,0,0.18);
  }
  .hero-art {
    position: absolute; left: 0; top: 0;
    width: 524px; height: 470px;
    background:
      radial-gradient(ellipse at 20% 25%, rgba(214,120,70,0.55), transparent 45%),
      radial-gradient(ellipse at 85% 15%, rgba(90,150,200,0.6), transparent 50%),
      radial-gradient(ellipse at 55% 45%, rgba(180,160,70,0.55), transparent 45%),
      radial-gradient(ellipse at 90% 60%, rgba(200,80,60,0.45), transparent 35%),
      linear-gradient(180deg, #b9cfdc 0%, #d7c9a8 45%, #9fc0d8 75%, rgba(217,230,238,0) 100%);
  }
  .brand {
    position: absolute; left: 28px; top: 100px;
    display: flex; align-items: center; gap: 8px;
    color: var(--brand-dark);
    font-size: 26px;
  }
  .brand-dot {
    width: 22px; height: 22px; border-radius: 50%;
    background: var(--brand-dark);
  }
  .title {
    position: absolute; right: 26px; top: 348px;
    text-align: right; color: var(--navy); line-height: 1;
  }
  .title .carp { display: block; font-size: 82px; }
  .title .fishing { display: block; font-size: 80px; margin-top: -4px; }
  .title .tournament { display: block; font-size: 50px; margin-top: 2px; }
  .details {
    position: absolute; left: 262px; width: 240px; top: 596px;
    text-align: center;
  }
  .date { color: var(--sage); font-size: 34px; letter-spacing: 0.5px; }
  .info { color: var(--navy); font-size: 18px; line-height: 1.45; margin-top: 12px; }
  .prize-badge { position: absolute; left: 0; top: 0; }
  .prize-list {
    position: absolute; left: 16px; width: 200px; top: 578px;
    text-align: center; list-style: none;
    color: var(--cream); font-size: 24px; line-height: 34px;
  }
  .sponsor-strip {
    position: absolute; left: 0; bottom: 0;
    width: 524px; height: 52px;
    background: var(--paper-edge);
  }
  .sponsor {
    position: absolute; left: 22px; top: 16px;
    display: flex; align-items: center; gap: 5px;
    color: var(--sponsor-orange); font-size: 16px;
  }
  .sponsor-mark { width: 10px; height: 10px; background: var(--sponsor-orange); }
</style>
</head>
<body>
  <main class="poster">
    <div class="hero-art" role="img" aria-label="Two carp leaping out of splashing water over a colourful grunge painted backdrop"></div>

    <div class="brand">
      <span class="brand-dot"></span>
      <span class="brand-name">Bramblewick</span>
    </div>

    <h1 class="title">
      <span class="carp">Carp</span>
      <span class="fishing">fishing</span>
      <span class="tournament">tournament</span>
    </h1>

    <div class="details">
      <p class="date">June 21st 2014</p>
      <p class="info">Minneapolis/St.Paul area<br>Cost to compete is $25</p>
    </div>

    <svg class="prize-badge" width="524" height="806" viewBox="0 0 524 806" aria-hidden="true">
      <polygon points="20,500 60,480 232,720 198,742" fill="var(--ribbon-tan)"/>
      <g fill="var(--badge-shadow)" transform="translate(-8,18)">
        <circle cx="116" cy="600" r="88"/>
        <circle cx="204" cy="600" r="24"/><circle cx="192" cy="644" r="24"/>
        <circle cx="160" cy="676" r="24"/><circle cx="116" cy="688" r="24"/>
        <circle cx="72" cy="676" r="24"/><circle cx="40" cy="644" r="24"/>
        <circle cx="28" cy="600" r="24"/><circle cx="40" cy="556" r="24"/>
      </g>
      <g fill="var(--badge-brown)">
        <circle cx="116" cy="600" r="88"/>
        <circle cx="204" cy="600" r="24"/><circle cx="192" cy="644" r="24"/>
        <circle cx="160" cy="676" r="24"/><circle cx="116" cy="688" r="24"/>
        <circle cx="72" cy="676" r="24"/><circle cx="40" cy="644" r="24"/>
        <circle cx="28" cy="600" r="24"/><circle cx="40" cy="556" r="24"/>
        <circle cx="72" cy="524" r="24"/><circle cx="116" cy="512" r="24"/>
        <circle cx="160" cy="524" r="24"/><circle cx="192" cy="556" r="24"/>
      </g>
      <path d="M116 536 v26 a8 8 0 0 1 -16 0 v-4" fill="none" stroke="var(--ribbon-tan)" stroke-width="3" stroke-linecap="round"/>
      <circle cx="116" cy="533" r="3" fill="none" stroke="var(--ribbon-tan)" stroke-width="2"/>
    </svg>

    <ul class="prize-list">
      <li>biggest fish</li>
      <li>ugliest fish</li>
      <li>most fish</li>
    </ul>

    <footer class="sponsor-strip">
      <div class="sponsor">
        <span class="sponsor-mark"></span>
        <span>Finbrawl</span>
      </div>
    </footer>
  </main>
</body>
</html>
```